Business card design for upmarket Home Technology design and Installation company

Hello designers, we need a great business card designed.
We need it to convey high tech, and also sophistication .
We work with some of the most affluent people in the world building them home technology systems, and A/V entertainment systems.

Services offered include the following:
Design, sales, installation, and maintenance of

*Home Automation systems
*Distributed / Multi-Room Audio and Video
*High Performance Networks & WiFi
* Lighting and Shade Control
*Home cinema
*Security and CCTV Systems

I have included a copy of our logo to use for your design efforts.

Target Market(s)

Upmarket clients with multi million euro villas.

Industry/Entity Type

Home technology

Contact Information for Business Card

NAME: Derek Halloran ADDRESS: Plaza Brisa Local 42, Port Calvera, 07392 PHONE: +34-602-518-794 EMAIL: DHalloran@VELTRAsmarthomes.com WEB: www.veltrasmarthomes.com

Requirements
Must have
• Our Logo, and our tagline

```html
<!DOCTYPE html>
<html lang="en">
<head>
<meta charset="utf-8">
<title>Veltra Business Card</title>
<link href="https://fonts.googleapis.com/css2?family=Arimo:ital,wght@0,400;0,700;1,400&display=swap" rel="stylesheet">
<style>
  :root {
    --backdrop: #c9c9c9;
    --card-white: #f7f7f5;
    --card-black: #111111;
    --gold: #c49a45;
    --ink: #1a1a1a;
    --divider: #cfcfcf;
    --tagline-light: #f2f2f2;
    --disc-faint: #1b1b1b;
  }
  * { margin: 0; padding: 0; box-sizing: border-box; }
  html, body {
    width: 1200px; height: 1051px; overflow: hidden;
    background: var(--backdrop);
    font-family: "Arimo", Arial, sans-serif;
  }
  .canvas { position: relative; width: 1200px; height: 1051px; }
  .card {
    position: absolute; left: 220px; width: 760px; height: 434px;
    overflow: hidden;
    box-shadow: 0 18px 40px rgba(0,0,0,0.22);
  }
  .card--front { top: 72px; background: var(--card-white); }
  .card--back { top: 546px; background: var(--card-black); }

  .brand { text-align: center; position: relative; }
  .brand__name {
    font-weight: 400; color: var(--gold);
    font-size: 60px; letter-spacing: 10px; line-height: 1;
  }
  .brand__tagline {
    font-style: italic; font-size: 19px; letter-spacing: 2.5px;
    margin-top: 6px; color: var(--ink);
  }
  .card--front .brand {
    position: absolute; left: 40px; width: 330px; top: 160px;
  }
  .card--front .divider {
    position: absolute; left: 396px; top: 120px; width: 1px; height: 194px;
    background: var(--divider);
  }
  .contact { position: absolute; left: 428px; top: 122px; color: var(--ink); }
  .contact__name {
    color: var(--gold); font-weight: 700; font-size: 24px; letter-spacing: 1.5px;
    margin-bottom: 20px;
  }
  .contact__address { font-size: 16px; line-height: 21px; margin-bottom: 14px; }
  .contact__line {
    display: flex; align-items: center; gap: 9px;
    font-size: 16px; line-height: 24px;
  }
  .contact__line svg { width: 13px; height: 13px; flex: none; }

  .back-disc {
    position: absolute; left: 60px; top: 40px; width: 300px; height: 300px;
    border-radius: 50%; background: var(--disc-faint);
  }
  .card--back .brand { position: absolute; left: 0; right: 0; top: 170px; }
  .card--back .brand__tagline { color: var(--tagline-light); }
</style>
</head>
<body>
<main class="canvas">
  <section class="card card--front">
    <div class="brand">
      <div class="brand__name">VELTRA</div>
      <div class="brand__tagline">Clever Living</div>
    </div>
    <div class="divider"></div>
    <div class="contact">
      <div class="contact__name">DEREK HALLORAN</div>
      <div class="contact__address">Plaza Brisa Local 42<br>Port Calvera, 07392</div>
      <div class="contact__line">
        <svg viewBox="0 0 24 24"><path fill="var(--gold)" d="M6.6 10.8a15 15 0 0 0 6.6 6.6l2.2-2.2a1 1 0 0 1 1-.25 11.4 11.4 0 0 0 3.6.57 1 1 0 0 1 1 1V20a1 1 0 0 1-1 1A17 17 0 0 1 3 4a1 1 0 0 1 1-1h3.5a1 1 0 0 1 1 1c0 1.25.2 2.45.57 3.57a1 1 0 0 1-.25 1z"/></svg>
        <span>+34-602-518-794</span>
      </div>
      <div class="contact__line">
        <svg viewBox="0 0 24 24"><path fill="var(--gold)" d="M2 5h20v14H2z"/><path fill="none" stroke="var(--card-white)" stroke-width="1.8" d="M2.5 5.5 12 13l9.5-7.5"/></svg>
        <span>DHalloran@VELTRAsmarthomes.com</span>
      </div>
      <div class="contact__line">
        <svg viewBox="0 0 24 24" fill="none" stroke="var(--gold)" stroke-width="2"><circle cx="12" cy="12" r="10"/><ellipse cx="12" cy="12" rx="4.5" ry="10"/><path d="M2 12h20M4 7h16M4 17h16"/></svg>
        <span>www.veltrasmarthomes.com</span>
      </div>
    </div>
  </section>

  <section class="card card--back">
    <div class="back-disc"></div>
    <div class="brand">
      <div class="brand__name">VELTRA</div>
      <div class="brand__tagline">Clever Living</div>
    </div>
  </section>
</main>
</body>
</html>
```